American cannabis tech company business card design

Thrum.com is seeking a modern, professional, and brand-aligned business card that represents our company and its core values: Mission, Story, Values, and Impact. As an innovative cannabis company, we want a business card that is not only visually appealing but also serves as a representation of who we are and what we stand for.

Project Scope: Design a double-sided business card that integrates our brand identity and core values. Incorporate our key brand elements, ensuring a sleek and contemporary aesthetic. Visually reflect our core values (Mission, Story, Values, Impact) in a way that is engaging yet professional.

Target Market(s)

Vendors, third parties,

Contact Information for Business Card

Contact details (name, title, email, phone, website, etc.)

Font styles to use
Other font styles liked:
• Caslon, Centra

Colors

Designer to choose colors to be used in the design.

Requirements
Must have
• Thrum.com logo and branding A creative yet clean way to integrate our core values (Mission, Story, Values, Impact) Modern typography and a well-structured layout
Nice to have
• forest green, grey, white, black
Should not have
• references to marijuana, leafs, plants, or related product

```html
<!DOCTYPE html>
<html lang="en">
<head>
<meta charset="utf-8">
<title>Thrum.com Business Card</title>
<link rel="stylesheet" href="https://fonts.googleapis.com/css2?family=Libre+Caslon+Text:wght@400;700&display=swap">
<style>
  :root {
    --forest: #143019;
    --ink-grey: #3a3d3a;
    --soft-grey: #7a7f7a;
    --card: #efefef;
    --backdrop: #dcdfdc;
  }
  * { margin: 0; padding: 0; box-sizing: border-box; }
  html, body {
    width: 1200px;
    height: 1200px;
    overflow: hidden;
    background: var(--backdrop);
    font-family: "Libre Caslon Text", Georgia, serif;
  }
  .canvas { position: relative; width: 1200px; height: 1200px; }
  .card {
    position: absolute;
    left: 247px;
    width: 704px;
    height: 402px;
    background: var(--card);
    border-radius: 4px;
  }
  .card--front { top: 130px; }
  .card--back { top: 590px; }

  .identity { position: absolute; left: 56px; top: 68px; }
  .identity__name {
    font-weight: 700;
    font-size: 22px;
    letter-spacing: 0.3px;
    color: var(--forest);
    line-height: 1.1;
  }
  .identity__title {
    font-size: 16px;
    color: var(--ink-grey);
    margin-top: 2px;
  }

  .contact-line {
    display: flex;
    align-items: center;
    gap: 10px;
    font-size: 17px;
    color: var(--ink-grey);
    position: absolute;
    line-height: 1;
  }
  .contact-line svg { width: 16px; height: 16px; fill: var(--forest); flex: none; }
  .contact-line--phone { right: 56px; top: 84px; }
  .contact-line--email { left: 56px; top: 290px; }
  .contact-line--web { left: 56px; top: 317px; }

  .core-values {
    position: absolute;
    font-size: 11px;
    letter-spacing: 3px;
    color: var(--soft-grey);
    text-transform: uppercase;
    white-space: nowrap;
  }
  .core-values span + span::before {
    content: "·";
    margin: 0 10px;
    color: var(--forest);
  }
  .core-values--front { left: 56px; top: 190px; }
  .core-values--back { left: 0; right: 0; top: 300px; text-align: center; }

  .wordmark {
    font-weight: 700;
    color: var(--forest);
    line-height: 1;
    letter-spacing: 0.5px;
    white-space: nowrap;
  }
  .wordmark--small {
    position: absolute;
    right: 56px;
    top: 290px;
    font-size: 46px;
  }
  .wordmark--large {
    position: absolute;
    left: 0;
    right: 0;
    top: 140px;
    text-align: center;
    font-size: 112px;
  }
</style>
</head>
<body>
<div class="canvas">
  <section class="card card--front">
    <div class="identity">
      <div class="identity__name">DANIEL REYES</div>
      <div class="identity__title">Owner</div>
    </div>

    <div class="contact-line contact-line--phone">
      <svg viewBox="0 0 24 24" aria-hidden="true"><path d="M6.6 10.8a15.1 15.1 0 0 0 6.6 6.6l2.2-2.2c.3-.3.7-.4 1-.2 1.1.4 2.3.6 3.6.6.6 0 1 .4 1 1V20c0 .6-.4 1-1 1A17 17 0 0 1 3 4c0-.6.4-1 1-1h3.5c.6 0 1 .4 1 1 0 1.3.2 2.5.6 3.6.1.3 0 .7-.2 1l-2.3 2.2z"/></svg>
      <span>+1 405-555-0148</span>
    </div>

    <div class="core-values core-values--front">
      <span>Mission</span><span>Story</span><span>Values</span><span>Impact</span>
    </div>

    <div class="contact-line contact-line--email">
      <svg viewBox="0 0 24 24" aria-hidden="true"><rect x="2" y="5" width="20" height="14"/><path d="M3 6.5l9 6.3 9-6.3" stroke="#efefef" stroke-width="1.6" fill="none"/></svg>
      <span>team@thrum.com</span>
    </div>
    <div class="contact-line contact-line--web">
      <svg viewBox="0 0 24 24" aria-hidden="true"><circle cx="12" cy="12" r="10"/><path d="M12 3.5v17M3.5 12h17M12 3.5c-3 3-3 14 0 17M12 3.5c3 3 3 14 0 17" stroke="#efefef" stroke-width="1.4" fill="none"/></svg>
      <span>www.thrum.com</span>
    </div>

    <div class="wordmark wordmark--small">THRUM</div>
  </section>

  <section class="card card--back">
    <div class="wordmark wordmark--large">THRUM</div>
    <div class="core-values core-values--back">
      <span>Mission</span><span>Story</span><span>Values</span><span>Impact</span>
    </div>
  </section>
</div>
</body>
</html>
```